Business card for a Exhibition booth fabrication company

Hi. My company would like to change our corporate name card. We are an events and Exhibition stand builder company. We would like our corporate name card to resonate what we do. I need someone to create something unique that relates to the industry that I am in. The graphic designer should be creative to incorporate the elements of my industry and try to blend in well in the design of the card. Our aim is to ensure that we are unique and our card can look different from our competitors.
Updates

The decision maker was very busy and didnt had time to make this decision

Target Market(s)

Marketing and events manager from all companies

Contact Information for Business Card

The business card should have the following details:
Name
Job Title
Email
Website

Colors

Designer to choose colors to be used in the design.

Requirements
Must have
• The card must be look something that is relevant to the service that I am providing. My website is: www.velmora-builds.com
• You can see my website to get more information on what service that I am doing
Nice to have
• On the back of my card, I would like to have a globe image with the incorporation of my company logo. This is to indicate that my services can be done in any part of the world.

```html
<!DOCTYPE html>
<html lang="en">
<head>
<meta charset="UTF-8">
<title>Velmora Builds – Business Card</title>
<link href="https://fonts.googleapis.com/css2?family=Montserrat:wght@500;600;700&family=Open+Sans:wght@400;600&display=swap" rel="stylesheet">
<style>
  :root {
    --bg: #1c1c1e;
    --card-dark: #2c2b2d;
    --card-light: #ffffff;
    --red: #e4242b;
    --grey: #58585a;
    --text-grey: #6b6b6d;
    --text-light: #f2f2f2;
    --map-tone: #3a393b;
  }
  * { margin: 0; padding: 0; box-sizing: border-box; }
  html, body { width: 1200px; height: 800px; overflow: hidden; }
  body {
    background: var(--bg);
    display: flex;
    align-items: center;
    justify-content: center;
    gap: 40px;
    font-family: "Open Sans", Arial, sans-serif;
  }
  .card {
    position: relative;
    width: 540px;
    height: 309px;
    overflow: hidden;
    box-shadow: 0 14px 30px rgba(0,0,0,0.5);
  }

  /* Back side */
  .card-back { background: var(--card-dark); color: var(--text-light); }
  .world-map {
    position: absolute;
    left: 70px; top: 20px;
    width: 400px; height: 190px;
    background: radial-gradient(ellipse at center, var(--map-tone) 0%, rgba(58,57,59,0.4) 55%, transparent 75%);
  }
  .services {
    position: absolute;
    left: 0; right: 0; top: 62px;
    display: flex;
    justify-content: center;
  }
  .service-list { list-style: none; font-size: 12.5px; line-height: 19px; }
  .service-list li { display: flex; align-items: center; gap: 8px; white-space: nowrap; }
  .service-list li::before, .service-list--left li::after {
    content: ""; width: 7px; height: 7px; background: var(--red); flex: none;
  }
  .service-list--left { text-align: right; padding-right: 12px; margin-top: 8px; }
  .service-list--left li { justify-content: flex-end; }
  .service-list--left li::before { display: none; }
  .service-divider { width: 1px; background: #bdbdbd; height: 92px; margin-top: 2px; }
  .service-list--right { padding-left: 12px; }
  .experience-band {
    position: absolute;
    left: 0; right: 0; bottom: 22px;
    height: 32px;
    background: var(--red);
    font-family: "Open Sans", Arial, sans-serif;
    font-size: 12.5px;
    letter-spacing: 0.3px;
    color: #fff;
    display: flex; align-items: center; justify-content: center;
  }

  /* Front side */
  .card-front { background: var(--card-light); }
  .brand {
    position: absolute;
    left: 0; right: 0; top: 62px;
    display: flex; align-items: center; justify-content: center; gap: 12px;
  }
  .brand-dot { width: 18px; height: 18px; border-radius: 50%; background: var(--red); }
  .brand-name {
    font-family: "Montserrat", Arial, sans-serif;
    font-weight: 700;
    font-size: 24px;
    letter-spacing: 3px;
    color: var(--grey);
  }
  .details {
    position: absolute;
    left: 0; right: 0; top: 136px;
    display: flex; justify-content: center; align-items: center;
  }
  .person { text-align: right; padding-right: 16px; }
  .person-name {
    font-family: "Montserrat", Arial, sans-serif;
    font-weight: 700; font-size: 20px; color: var(--red);
  }
  .person-title { font-size: 13px; color: var(--text-grey); }
  .details-divider { width: 1px; height: 58px; background: var(--red); }
  .contacts { list-style: none; padding-left: 16px; font-size: 12px; color: var(--text-grey); line-height: 20px; }
  .contacts li { display: flex; align-items: center; gap: 8px; }
  .contacts svg { width: 11px; height: 11px; fill: var(--red); flex: none; }
  .contacts .web-accent { color: var(--red); }
  .front-band {
    position: absolute; left: 0; right: 0; bottom: 0; height: 12px;
    display: flex;
  }
  .front-band-red { flex: 0 0 62%; background: var(--red); }
  .front-band-grey { flex: 1; background: var(--grey); }
</style>
</head>
<body>

  <section class="card card-back">
    <div class="world-map" role="img" aria-label="Faint dotted world map"></div>
    <div class="services">
      <ul class="service-list service-list--left">
        <li>Exhibition Booth Fabrication</li>
        <li>Outdoor Booth Setup</li>
        <li>Interior Design</li>
        <li>Installation and Dismantle</li>
      </ul>
      <div class="service-divider"></div>
      <ul class="service-list service-list--right">
        <li>Exhibition Management</li>
        <li>Shell Scheme Display Booth</li>
        <li>Custom Stand Design</li>
        <li>Exhibition Furniture and Equipment</li>
        <li>Exhibition Project Management</li>
      </ul>
    </div>
    <div class="experience-band">OVER 20 YEARS EXPERIENCE OF EXHIBITION STAND SERVICES</div>
  </section>

  <section class="card card-front">
    <div class="brand">
      <span class="brand-dot"></span>
      <span class="brand-name">VELMORA BUILDS</span>
    </div>
    <div class="details">
      <div class="person">
        <div class="person-name">Alden Marsh</div>
        <div class="person-title">Director</div>
      </div>
      <div class="details-divider"></div>
      <ul class="contacts">
        <li>
          <svg viewBox="0 0 24 24" aria-hidden="true"><path d="M6.6 10.8a15.1 15.1 0 0 0 6.6 6.6l2.2-2.2a1 1 0 0 1 1-.25 11.4 11.4 0 0 0 3.6.57 1 1 0 0 1 1 1V20a1 1 0 0 1-1 1A17 17 0 0 1 3 4a1 1 0 0 1 1-1h3.5a1 1 0 0 1 1 1c0 1.25.2 2.45.57 3.57a1 1 0 0 1-.25 1z"/></svg>
          0198 765 432
        </li>
        <li>
          <svg viewBox="0 0 24 24" aria-hidden="true"><path d="M2 5h20v14H2zm2 2v.5l8 5 8-5V7zm0 2.9V17h16V9.9l-8 5z"/></svg>
          hello@velmora-builds.com
        </li>
        <li>
          <svg viewBox="0 0 24 24" aria-hidden="true"><path d="M12 2a10 10 0 1 0 0 20 10 10 0 0 0 0-20zm6.9 6h-3a15 15 0 0 0-1.3-3.9A8 8 0 0 1 18.9 8zM12 4c.8 1.2 1.5 2.5 1.9 4h-3.8c.4-1.5 1.1-2.8 1.9-4zM4.3 14a8 8 0 0 1 0-4h3.4a16 16 0 0 0 0 4zm.8 2h3a15 15 0 0 0 1.3 3.9A8 8 0 0 1 5.1 16zm3-8h-3a8 8 0 0 1 4.3-3.9A15 15 0 0 0 8.1 8zM12 20c-.8-1.2-1.5-2.5-1.9-4h3.8c-.4 1.5-1.1 2.8-1.9 4zm2.3-6H9.7a14 14 0 0 1 0-4h4.6a14 14 0 0 1 0 4zm.3 5.9a15 15 0 0 0 1.3-3.9h3a8 8 0 0 1-4.3 3.9zm1.7-5.9a16 16 0 0 0 0-4h3.4a8 8 0 0 1 0 4z"/></svg>
          <span>www.<span class="web-accent">velmora-builds</span>.com</span>
        </li>
      </ul>
    </div>
    <div class="front-band">
      <div class="front-band-red"></div>
      <div class="front-band-grey"></div>
    </div>
  </section>

</body>
</html>
```